Business Card Design

We sell fish products to corporate food companies who then turn these products into final food products for consumers

Industry/Entity Type

Business

Contact Information for Business Card

I need a corporate business card template for a fish products business. We would like it be professional for use in dealing with multi national companies. This company business card template will be used by multiple employees so the following fields must be open to edit (Name, Phone Number and Email address)

```html
<!DOCTYPE html>
<html lang="en">
<head>
<meta charset="utf-8">
<title>Tidewater Harvest – Business Card</title>
<link rel="stylesheet" href="https://fonts.googleapis.com/css2?family=Arimo:wght@400;700&display=swap">
<style>
  :root {
    --stage: #3a3a3c;
    --brand-blue: #0b5ca8;
    --brand-blue-light: #2c7fcf;
    --brand-blue-deep: #0a4f93;
    --paper: #ffffff;
    --ink-white: #ffffff;
    --icon-green: #3fa34d;
  }
  * { margin: 0; padding: 0; box-sizing: border-box; }
  html, body {
    width: 1200px; height: 1000px; overflow: hidden;
    background: var(--stage);
    font-family: "Arimo", Arial, sans-serif;
  }
  .sheet { position: relative; width: 1200px; height: 1000px; }
  .card {
    position: absolute; left: 337px; width: 525px; height: 300px;
    overflow: hidden; box-shadow: 0 10px 30px rgba(0,0,0,.45);
  }
  .card-front { top: 150px; background: var(--paper); }
  .card-back  { top: 540px; background: var(--brand-blue); }
  .card svg.shapes { position: absolute; inset: 0; }

  .brand-lockup {
    position: absolute; display: flex; align-items: center; gap: 10px;
    color: var(--brand-blue); font-weight: 700; letter-spacing: .5px;
    white-space: nowrap;
  }
  .brand-lockup .brand-dot {
    border-radius: 50%; background: var(--brand-blue); flex: none;
  }
  .card-front .brand-lockup { left: 160px; top: 133px; font-size: 26px; }
  .card-front .brand-dot { width: 34px; height: 34px; }

  .card-back .brand-lockup {
    right: 24px; top: 34px; font-size: 16px; line-height: 1.15; gap: 8px;
  }
  .card-back .brand-name { display: flex; flex-direction: column; }
  .card-back .brand-dot { width: 20px; height: 20px; }

  .holder-name {
    position: absolute; left: 38px; top: 92px;
    color: var(--ink-white); font-weight: 700; font-size: 28px; letter-spacing: 1px;
  }
  .contact-list { position: absolute; left: 38px; top: 142px; list-style: none; }
  .contact-list li {
    display: flex; align-items: center; gap: 10px; height: 28px;
    color: var(--ink-white); font-weight: 700; font-size: 17px;
  }
  .contact-list li:first-child { font-size: 21px; }
  .contact-icon { width: 22px; height: 22px; flex: none; }
  .company-block { position: absolute; left: 38px; bottom: 24px; color: var(--ink-white); }
  .company-name { font-weight: 700; font-size: 15px; letter-spacing: .5px; }
  .company-address { font-size: 11px; margin-top: 2px; }
</style>
</head>
<body>
<main class="sheet">

  <section class="card card-front" aria-label="Card front">
    <svg class="shapes" width="525" height="300" viewBox="0 0 525 300">
      <path d="M0 0 H120 Q20 140 70 300 H0 Z" fill="var(--brand-blue-light)"/>
      <path d="M0 0 H100 Q0 140 55 300 H0 Z" fill="var(--brand-blue)"/>
    </svg>
    <div class="brand-lockup">
      <span class="brand-dot"></span>
      <span class="brand-name">TIDEWATER HARVEST</span>
    </div>
  </section>

  <section class="card card-back" aria-label="Card back">
    <svg class="shapes" width="525" height="300" viewBox="0 0 525 300">
      <polygon points="270,0 525,0 525,220" fill="var(--brand-blue-deep)" opacity=".35"/>
      <polygon points="280,0 525,0 525,200 410,155" fill="var(--paper)"/>
    </svg>
    <div class="brand-lockup">
      <span class="brand-dot"></span>
      <span class="brand-name"><span>TIDEWATER</span><span>HARVEST</span></span>
    </div>

    <h1 class="holder-name">DANA WHITLOCK</h1>
    <ul class="contact-list">
      <li>
        <svg class="contact-icon" viewBox="0 0 22 22" aria-hidden="true">
          <circle cx="11" cy="11" r="11" fill="#fff"/>
          <path d="M7 5 L9.5 5 L10.5 8 L9 9 Q10 12 13 13 L14 11.5 L17 12.5 L17 15 Q11 17 7 11 Q5 8 7 5 Z" fill="var(--icon-green)"/>
        </svg>
        <span class="contact-phone">555-014-2290</span>
      </li>
      <li>
        <svg class="contact-icon" viewBox="0 0 22 22" aria-hidden="true">
          <circle cx="11" cy="11" r="11" fill="#fff"/>
          <rect x="5" y="7" width="12" height="8" fill="var(--icon-green)"/>
          <path d="M5 7 L11 12 L17 7" fill="none" stroke="#fff" stroke-width="1.2"/>
        </svg>
        <span class="contact-email">tidewaterusa@mailbox.com</span>
      </li>
      <li>
        <svg class="contact-icon" viewBox="0 0 22 22" aria-hidden="true">
          <circle cx="11" cy="11" r="11" fill="#fff"/>
          <circle cx="11" cy="11" r="6.5" fill="none" stroke="var(--icon-green)" stroke-width="1.5"/>
          <ellipse cx="11" cy="11" rx="2.8" ry="6.5" fill="none" stroke="var(--icon-green)" stroke-width="1.2"/>
          <line x1="4.5" y1="11" x2="17.5" y2="11" stroke="var(--icon-green)" stroke-width="1.2"/>
        </svg>
        <span class="contact-web">www.tidewaterusa.com</span>
      </li>
    </ul>

    <div class="company-block">
      <p class="company-name">TIDEWATER HARVEST</p>
      <p class="company-address">4410 River Bend Road Marlow, KY 40000 USA</p>
    </div>
  </section>

</main>
</body>
</html>
```